Design a cool print brochure for an NGO / Give your work a global impact!!

Hi,
I provide a full design brief (below, please scroll) and a mood board (attached) to help you visualize inside my head.. ;-)
I am also available to help and have worked many years in advertising; we will understand each other.
Objective:
To design an A4 folded in two presentation brochure for a non-profit consulting agency called Mer-ova.
Mer-ova works in sustainability and international development = working with NGO’s, governments and private sector on global issues such as global warming, education for all etc.
Strategy:
This document is a first step in developing a communication strategy. It will be distributed during a major international event called the Brenvik Outreach Forum.
Objective:
The double objective of the brochure is:
a) to inform the recipient of what Mer-ova is, in the shortest time possible.
b) to showcase relevant projects to demonstrate Mer-ova experience and expertise.
Target:
Main target:
Existing Mer-ova contacts, such as members of development organizations, NGOs, private sector foundations (CSR), regional networks and other development actors.
NB: the main target already has a certain awareness of Mer-ova: we will try to minimize text to maximize visual impact and readability.
Secondary target:
Mer-ova will also distribute the brochure to new prospects of interest during the Brenvik Forum.
Timing:
We will need to finalize the design and have the files by June 1st to allow time for print before the event.
Content:
The document should be concise, highly readable (no clutter) and include:
1. text (that we will provide)
and
2. visual elements such as images, shapes and info-graphics (that is you).
NB: Mer-ova does not have its own image bank; photos will be provided by you.
Format:
A4 folded in half - 4pp A5 - PORTRAIT FORMAT) with an impactful visual in the front, logo, title and headline (please see examples in the mood board attached).
Design elements:
Mer-ova does not have yet a visual identity (please see: http://mer-ova.org) so there is room for creativity and no graphic chart to follow.
The sector of consulting in international development is rather conservative but our intention is to be disruptive and create a “Wow” effect. We count on you for that!
Therefore, the design should be “structured”, “organized”, “uncluttered” but also “modern”, “impactful”, “highly visual” (think infographic or mind map to describe our services and projects).
Please, take the time to see the attached presentation: I give you guidelines and examples of what we want and what we like.
We are looking forward to seeing your work and I am available for comments, questions and support.
Thank you.
RM
Target Market(s)
The full brief is in the project description: please, scroll through it.
The target market is : our existing clients base, working in sustainable development (read: NGO and Concord Assembly people)
Industry/Entity Type
Ngo
Requirements
Must have
- - Design and color elements: please, no black and white. Our company website is in black and white and without graphics; we want the brochure to break away from that and start creating our brand identity; so please, show us colors and desing elements (shapes, backgrounds, etc).
- You have a chance to showcase your talent in terms of visual identity: what lines, forms, layout and colors can you come up with and apply throughout the brochure and serve as the visual identity of Mer-ova?
- The structure of the document should be:
- - Front cover: design elements + impacful photo (see mood board example attached) +our logo + this headline: "Collective action for sustainable development and impact"
- - Inside front: a graphic representation of "Our Services": such as core activity in the center circle and satellite circles for the services we offer.
- - Inside back:
- 1. Icons and text boxes for "Our projects"
- 2. A world map of the countries where we have worked. Full list of countries is here:
- http://mer-ova.org/experience-1
- - Back cover: our contact + logos of partners.
- Our partners are listed here:
- Please use their original logos (ie, in color).
- The design we will select will serve as a basis for a graphic chart...so more work to come...word to the wise ;)
- Please check out our website mer-ova.org to see what we do etc.
Nice to have
- Icons to reflect our services: what icons can you come up with to describe "training services", "building networks" or "program management"?
- I give examples in the mood board.
Should not have
- We are open to creativity and want to generate a "Wow" effect.
- Just note that the sector is rather conservative so flashy colors and cartoon like characters should be avoided. Think "earth, global change, Concord Assembly, climate" without going too green (it's overdone). ;-)
- Make us stand out in the NGO world
- Now you.

```html
<!DOCTYPE html>
<html lang="en">
<head>
<meta charset="utf-8">
<title>Mer-ova Brochure</title>
<link href="https://fonts.googleapis.com/css2?family=Montserrat:wght@500;600;700;800&family=Open+Sans:wght@400;600&display=swap" rel="stylesheet">
<style>
  :root{
    --teal:#17a88a;
    --teal-dark:#0f8a71;
    --navy:#263a5e;
    --red:#c8362f;
    --orange:#f29b1d;
    --sky:#dcf0fa;
    --ink:#3a4656;
    --muted:#8a96a3;
    --stage:#ececec;
    --paper:#ffffff;
  }
  *{box-sizing:border-box;margin:0;padding:0}
  html,body{width:668px;height:1200px;overflow:hidden;background:var(--stage)}
  body{font-family:"Open Sans",Arial,sans-serif;color:var(--ink);position:relative}
  .spread{position:absolute;left:0;width:668px;height:472px;background:var(--paper);overflow:hidden;box-shadow:0 2px 8px rgba(0,0,0,.12)}
  .spread--outer{top:110px}
  .spread--inner{top:600px}
  .page{position:absolute;top:0;width:334px;height:472px}
  .page--left{left:0}
  .page--right{left:334px}
  .heading{font-family:"Montserrat",Arial,sans-serif;font-weight:800;font-style:italic;color:var(--teal);font-size:12px;letter-spacing:.5px;text-transform:uppercase}
  .rule{height:1.5px;background:var(--teal);opacity:.5;margin-top:5px;width:250px}

  /* back cover */
  .contact{position:absolute;left:52px;top:150px}
  .contact-list{list-style:none;margin-top:12px}
  .contact-list li{display:flex;align-items:center;gap:8px;font-size:8px;color:var(--ink);margin-bottom:8px}
  .contact-list svg{width:9px;height:9px;fill:var(--teal)}
  .partners{position:absolute;left:52px;top:262px}
  .partner-grid{display:grid;grid-template-columns:repeat(3,70px);gap:14px 18px;margin-top:16px}
  .partner{height:24px;border-radius:3px;background:#dde3e8}
  .partner:nth-child(3n+2){background:#d2dbe3}

  /* front cover */
  .cover-photo{position:absolute;left:0;top:0}
  .cover-band{position:absolute;left:0;top:250px;width:10px;height:222px;background:var(--teal)}
  .cover-title{position:absolute;left:26px;top:272px;font-family:"Montserrat",Arial,sans-serif;font-weight:800;font-size:19px;line-height:1.12;color:var(--teal);text-transform:uppercase;width:250px}
  .cover-footer{position:absolute;left:0;top:418px;width:334px;height:24px}
  .cover-url{position:absolute;left:10px;top:0;height:24px;width:150px;background:var(--teal);color:#fff;font-size:8px;font-weight:600;display:flex;align-items:center;gap:6px;padding-left:16px}
  .cover-url svg{width:9px;height:9px;fill:#fff}
  .brand{position:absolute;right:26px;top:0;height:24px;display:flex;align-items:center;gap:7px;font-family:"Open Sans",Arial,sans-serif;font-weight:600;font-size:17px;color:var(--teal);letter-spacing:1.5px;text-transform:uppercase}
  .brand-dot{width:12px;height:12px;border-radius:50%;background:var(--teal)}

  /* inside left */
  .services{position:absolute;inset:0;background:linear-gradient(180deg,var(--sky) 0%,#eef8fd 55%,#ffffff 100%)}
  .services svg text{font-family:"Montserrat",Arial,sans-serif;font-weight:700;text-transform:uppercase}

  /* inside right */
  .map{position:absolute;left:14px;top:18px;width:306px;height:130px;border-radius:6px;background:linear-gradient(180deg,#eef1f3,#f7f8f9)}
  .projects-title{position:absolute;left:0;top:158px;width:334px;text-align:center}
  .project{position:absolute;left:16px;width:304px;height:56px;display:flex;gap:6px}
  .region{width:66px;height:56px;border-radius:4px;display:flex;align-items:center;justify-content:center;color:#fff;font-family:"Montserrat",Arial,sans-serif;font-weight:800;font-size:9px;text-transform:uppercase}
  .region--europe{background:var(--red)}
  .region--america{background:var(--teal)}
  .region--asia{background:var(--navy)}
  .region--africa{background:var(--teal-dark)}
  .countries{flex:1;border:1.5px solid var(--teal);border-radius:8px;padding:6px 9px;font-size:7.4px;line-height:1.45;display:flex;align-items:center;color:var(--ink)}
</style>
</head>
<body>

<section class="spread spread--outer">
  <div class="page page--left">
    <div class="contact">
      <h2 class="heading">Contact us</h2>
      <div class="rule"></div>
      <ul class="contact-list">
        <li><svg viewBox="0 0 24 24"><path d="M6.6 10.8a15 15 0 006.6 6.6l2.2-2.2a1 1 0 011-.25 11.4 11.4 0 003.6.57 1 1 0 011 1V20a1 1 0 01-1 1A17 17 0 013 4a1 1 0 011-1h3.5a1 1 0 011 1c0 1.250.2 2.45.57 3.6a1 1 0 01-.25 1z"/></svg>+00 555 010 246</li>
        <li><svg viewBox="0 0 24 24"><path d="M2 5h20v14H2zm2 2v.4l8 5 8-5V7l-8 5z"/></svg>info@mer-ova.org</li>
        <li><svg viewBox="0 0 24 24"><circle cx="12" cy="12" r="10"/></svg>www.mer-ova.org</li>
      </ul>
    </div>
    <div class="partners">
      <h2 class="heading">Our partners</h2>
      <div class="rule"></div>
      <div class="partner-grid" aria-label="Partner badges">
        <div class="partner"></div><div class="partner"></div><div class="partner"></div>
        <div class="partner"></div><div class="partner"></div><div class="partner"></div>
        <div class="partner"></div><div class="partner"></div><div class="partner"></div>
      </div>
    </div>
  </div>

  <div class="page page--right">
    <svg class="cover-photo" width="334" height="260" viewBox="0 0 334 260">
      <defs>
        <linearGradient id="photoTone" x1="0" y1="0" x2="1" y2="1">
          <stop offset="0" stop-color="#7d8c95"/>
          <stop offset=".5" stop-color="#b9a89a"/>
          <stop offset="1" stop-color="#5d6b78"/>
        </linearGradient>
        <clipPath id="photoClip"><circle cx="210" cy="112" r="140"/></clipPath>
      </defs>
      <rect width="334" height="260" fill="#fff"/>
      <g clip-path="url(#photoClip)">
        <rect x="60" y="-30" width="280" height="290" fill="url(#photoTone)" role="img" aria-label="Photo of a team of young professionals collaborating around laptops"/>
      </g>
      <circle cx="210" cy="112" r="144" fill="none" stroke="var(--teal)" stroke-width="7"/>
      <circle cx="210" cy="112" r="154" fill="none" stroke="var(--teal)" stroke-width="1.5" opacity=".5"/>
    </svg>
    <div class="cover-band"></div>
    <h1 class="cover-title">Collective action for sustainable development and impact</h1>
    <div class="cover-footer">
      <div class="cover-url"><svg viewBox="0 0 24 24"><circle cx="12" cy="12" r="10"/></svg>www.mer-ova.org</div>
      <div class="brand"><span class="brand-dot"></span>Mer-ova</div>
    </div>
  </div>
</section>

<section class="spread spread--inner">
  <div class="page page--left services">
    <svg width="334" height="472" viewBox="0 0 334 472">
      <g stroke="#9fb4c4" stroke-width="1.5">
        <line x1="167" y1="236" x2="72" y2="132"/>
        <line x1="167" y1="236" x2="152" y2="92"/>
        <line x1="167" y1="236" x2="250" y2="126"/>
        <line x1="167" y1="236" x2="74" y2="344"/>
        <line x1="167" y1="236" x2="160" y2="388"/>
        <line x1="167" y1="236" x2="254" y2="352"/>
      </g>
      <circle cx="167" cy="236" r="60" fill="var(--teal)" stroke="#fff" stroke-width="5"/>
      <text x="167" y="233" text-anchor="middle" fill="#fff" font-size="13">Mer-ova</text>
      <text x="167" y="250" text-anchor="middle" fill="#fff" font-size="11">Services</text>

      <g font-size="5.2" fill="var(--ink)" text-anchor="middle">
        <circle cx="72" cy="132" r="38" fill="#fff" stroke="var(--red)" stroke-width="5"/>
        <text x="72" y="124">Research and</text><text x="72" y="131">analysis of</text><text x="72" y="138">cooperation</text><text x="72" y="145">schemes</text>

        <circle cx="152" cy="92" r="38" fill="#fff" stroke="var(--orange)" stroke-width="5"/>
        <text x="152" y="84">Facilitation of</text><text x="152" y="91">processes of</text><text x="152" y="98">change</text>

        <circle cx="250" cy="126" r="38" fill="#fff" stroke="var(--navy)" stroke-width="5"/>
        <text x="250" y="118">Training</text><text x="250" y="125">to improve</text><text x="250" y="132">the impact of</text><text x="250" y="139">actions</text>

        <circle cx="74" cy="344" r="38" fill="#fff" stroke="var(--red)" stroke-width="5"/>
        <text x="74" y="333">Networking for</text><text x="74" y="340">knowledge</text><text x="74" y="347">sharing and</text><text x="74" y="354">community building</text>

        <circle cx="160" cy="388" r="38" fill="#fff" stroke="var(--orange)" stroke-width="5"/>
        <text x="160" y="380">Evaluation of</text><text x="160" y="387">multi-sector</text><text x="160" y="394">projects and</text><text x="160" y="401">programs</text>

        <circle cx="254" cy="352" r="38" fill="#fff" stroke="var(--teal)" stroke-width="5"/>
        <text x="254" y="344">Coaching</text><text x="254" y="351">sessions to</text><text x="254" y="358">achieve collective</text><text x="254" y="365">goals</text>
      </g>
    </svg>
  </div>

  <div class="page page--right">
    <div class="map" role="img" aria-label="World map marking the countries where projects were delivered"></div>
    <h2 class="heading projects-title">Our projects</h2>

    <div class="project" style="top:186px">
      <div class="region region--europe">Europe</div>
      <p class="countries">EU, DE, Norway, Switzerland, Turkey, Montenegro, Ukraine, Serbia, Moldova, Armenia, Georgia and Belarus.</p>
    </div>
    <div class="project" style="top:250px">
      <div class="region region--america">America</div>
      <p class="countries">US, Canada, Guatemala, El Salvador, Panama, Costa Rica, Honduras, Colombia, Peru, Bolivia, Brazil, Argentina, Uruguay and Paraguay.</p>
    </div>
    <div class="project" style="top:314px">
      <div class="region region--asia">Asia</div>
      <p class="countries">China, Vietnam, Thailand, Indonesia, Malaysia, Singapore, Bangladesh, Kyrgyzstan, Kazakhstan and Myanmar.</p>
    </div>
    <div class="project" style="top:378px">
      <div class="region region--africa">Africa</div>
      <p class="countries">South Africa, Mozambique, Ethiopia, Kenya, Uganda, Benin, Senegal, Zimbabwe, Ghana, Tunisia, Egypt and Libya.</p>
    </div>
  </div>
</section>

</body>
</html>
```